MAPLE KEYS PROPERTY MANAGEMENT INC. WEBSITE

Please make the website more family-friendly.

I want a website to help me build my property management business by adding listing properties and creating an online application. Im open to any other ideas.
I want a WordPress designer to code it.

Here is my current website. www.maplekeys.biz

IDEA: I like the website design https://www.bluffcoveheatingandair.com/

Thank you

Tom

```html
<!DOCTYPE html>
<html lang="en">
<head>
<meta charset="utf-8">
<title>Maple Keys Property Management Inc.</title>
<link href="https://fonts.googleapis.com/css2?family=Oswald:wght@500;700&family=Poppins:wght@400;500;600;700;800&display=swap" rel="stylesheet">
<style>
:root{
  --red:#b3121b;
  --red-dark:#8e0c13;
  --ink:#1c1c1c;
  --muted:#6b6b6b;
  --line:#e3e3e3;
  --pink:#f7d9dc;
  --dark:#23262b;
  --white:#ffffff;
  --bg:#ffffff;
}
*{box-sizing:border-box;margin:0;padding:0}
html,body{width:1200px;height:2620px;overflow:hidden;background:var(--bg)}
body{font-family:"Poppins",sans-serif;color:var(--ink);position:relative}
.page{position:relative;width:1200px;height:2620px;overflow:hidden}
.btn{display:inline-block;background:var(--red);color:var(--white);font-size:11px;font-weight:600;letter-spacing:.5px;text-transform:uppercase;padding:11px 24px;border-radius:20px}
.photo{border-radius:14px}
h2.section-title{font-family:"Oswald",sans-serif;font-weight:700;font-size:44px;letter-spacing:1px;text-align:center;text-transform:uppercase}

/* header */
.site-header{position:absolute;top:0;left:0;width:1200px;height:80px;display:flex;align-items:center;justify-content:space-between;padding:0 100px}
.brand{display:flex;align-items:center;gap:10px}
.brand-mark{width:30px;height:30px;background:var(--red);border-radius:50%}
.brand-name{font-weight:700;font-size:20px;color:var(--red);letter-spacing:.5px}
.main-nav{display:flex;align-items:center;gap:22px;font-size:10px;font-weight:600;text-transform:uppercase}
.main-nav .active{color:var(--red)}
.main-nav .btn{padding:8px 14px;font-size:10px;border-radius:4px}

/* hero */
.hero{position:absolute;top:110px;left:100px;width:1000px;height:400px}
.hero-copy{position:absolute;left:60px;top:75px;width:380px}
.hero-kicker{color:var(--red);font-weight:700;font-size:14px;text-transform:uppercase}
.hero-title{font-weight:800;font-size:42px;line-height:1.1;margin:8px 0 16px}
.hero-text{font-size:11px;color:var(--muted);line-height:1.7;margin-bottom:24px}
.hero-photo-main{position:absolute;left:440px;top:20px;width:310px;height:340px;background:linear-gradient(160deg,#6d7d8f,#3a3a36 60%,#a0763f)}
.hero-photo-side{position:absolute;left:760px;top:20px;width:220px;height:340px;background:linear-gradient(170deg,#d7cfc4,#8e6e57 70%,#5b4030)}

/* about intro */
.about-arc{position:absolute;top:540px;left:0;width:1200px;height:180px}
.about-intro{position:absolute;top:600px;left:0;width:1200px;text-align:center}
.about-intro p{width:560px;margin:14px auto 0;font-size:11px;color:var(--muted);line-height:1.7}

/* about detail */
.about-detail{position:absolute;top:770px;left:160px;width:880px;height:330px}
.about-photo-main{position:absolute;left:0;top:0;width:300px;height:250px;background:linear-gradient(180deg,#8fb7d8,#d9d9d4 55%,#5f8a44)}
.about-photo-small{position:absolute;left:170px;top:120px;width:150px;height:120px;background:linear-gradient(180deg,#a9c8e2,#cfcac0 55%,#6d8f4c);border:4px solid var(--white)}
.about-body{position:absolute;left:410px;top:20px;width:470px}
.about-body h3{font-weight:700;font-size:15px;line-height:1.35;text-transform:uppercase}
.about-body p{font-size:11px;color:var(--muted);line-height:1.7;margin:12px 0 16px}
.checks{display:grid;grid-template-columns:1fr 1fr;gap:8px 30px;font-size:11px;margin-bottom:24px}
.checks li{list-style:none;display:flex;align-items:center;gap:8px}

/* listing */
.listing{position:absolute;top:1170px;left:0;width:1200px}
.listing-lead{text-align:center;font-size:11px;color:var(--muted);width:560px;margin:10px auto 0;line-height:1.7}
.cards{position:absolute;top:140px;left:100px;width:1000px;display:flex;gap:20px}
.card{width:320px}
.card-photo{height:195px;border-radius:6px}
.card h4{font-size:12px;font-weight:600;margin:16px 0 8px}
.card p{font-size:10px;color:var(--muted);line-height:1.6}
.card-meta{display:flex;gap:16px;font-size:10px;color:var(--muted);margin-top:12px}
.slider-arrow{position:absolute;top:225px;width:24px;height:24px;border-radius:50%}
.listing-more{position:absolute;top:500px;left:0;width:1200px;text-align:center}

/* testimonials */
.testimonials{position:absolute;top:1775px;left:0;width:1200px;height:420px;background:linear-gradient(180deg,#2f3439 0%,#3c4249 45%,#1f2226 100%)}
.testimonials h2{color:var(--white);margin-top:60px}
.quotes{position:absolute;top:160px;left:160px;width:880px;display:flex;gap:40px}
.quote{width:267px;color:var(--white)}
.quote-mark{font-family:"Oswald",sans-serif;font-size:40px;line-height:1}
.quote p{font-size:11px;line-height:1.7;color:#e6e6e6;margin:4px 0 18px}
.author{display:flex;align-items:center;gap:14px;font-size:12px;font-weight:600}
.avatar{width:48px;height:48px;border-radius:50%;background:linear-gradient(160deg,#c79b7c,#6a4a3a);border:2px solid var(--white)}
.testi-arrow{position:absolute;top:210px;width:22px;height:22px;border-radius:50%}

/* contact */
.contact{position:absolute;top:2265px;left:100px;width:1000px;height:290px}
.contact-info{position:absolute;left:60px;top:0;width:340px}
.contact-kicker{color:var(--red);font-size:10px;font-weight:600;text-transform:uppercase}
.contact-info h2{font-family:"Oswald",sans-serif;font-size:34px;font-weight:700;text-transform:uppercase;line-height:1.1}
.contact-info h5{font-size:11px;font-weight:700;text-transform:uppercase;margin:18px 0 10px}
.info-row{display:flex;gap:10px;font-size:10px;color:var(--muted);line-height:1.5;margin-bottom:8px}
.call-label{font-size:10px;font-weight:700;text-transform:uppercase;margin-top:14px}
.call-number{font-size:20px;font-weight:700}
.contact-form{position:absolute;left:420px;top:0;width:520px;display:grid;grid-template-columns:1fr 1fr;gap:14px 16px}
.field{border:1px solid var(--line);height:40px;font-size:10px;color:#999;padding:12px 14px;border-radius:3px}
.field.message{grid-column:1 / span 2;height:110px}
.submit{grid-column:1 / span 2;justify-self:end}
.submit .btn{background:var(--ink);border-radius:4px;padding:11px 36px}

/* footer */
.site-footer{position:absolute;top:2580px;left:0;width:1200px;height:40px;background:var(--red);display:flex;align-items:center;justify-content:space-between;padding:0 100px;color:var(--white);font-size:10px}
.socials{display:flex;gap:8px}
.socials span{width:20px;height:20px;border-radius:50%;border:1.5px solid var(--white)}
</style>
</head>
<body>
<div class="page">

<header class="site-header">
  <div class="brand"><span class="brand-mark"></span><span class="brand-name">MAPLE KEYS</span></div>
  <nav class="main-nav">
    <span class="active">Listings</span><span>Owners</span><span>Property Owners</span><span>About</span><span>Community</span><span>Portfolio Info</span><span class="btn">Contact Us</span>
  </nav>
</header>

<section class="hero">
  <div class="hero-copy">
    <div class="hero-kicker">Get 1 Month Property</div>
    <h1 class="hero-title">Management Fee Off. $120 Value!</h1>
    <p class="hero-text">Whether you are an experienced investor or a first-time home owner, we are here to help you find the right home for your family and keep your property in great shape all year long.</p>
    <span class="btn">Contact Us</span>
  </div>
  <div class="photo hero-photo-main" role="img" aria-label="Modern two-storey family home at dusk with a lit fire pit"></div>
  <div class="photo hero-photo-side" role="img" aria-label="Warm living room interior with sofa and rug"></div>
</section>

<svg class="about-arc" viewBox="0 0 1200 180" preserveAspectRatio="none" aria-hidden="true">
  <defs><linearGradient id="arcFill" x1="0" y1="0" x2="0" y2="1"><stop offset="0" stop-color="#f4c6cb"/><stop offset="1" stop-color="#ffffff" stop-opacity="0"/></linearGradient></defs>
  <path d="M0 180 Q600 -40 1200 180 Z" fill="url(#arcFill)"/>
</svg>

<section class="about-intro">
  <h2 class="section-title">About Us</h2>
  <p>Renting the right property should feel simple. Our team is committed to helping owners and families with leasing, upkeep and friendly service. We believe clear communication builds lasting trust between residents and owners in our community.</p>
</section>

<section class="about-detail">
  <div class="photo about-photo-main" role="img" aria-label="Two-storey suburban house with green lawn"></div>
  <div class="photo about-photo-small" role="img" aria-label="Front view of a bright family home"></div>
  <div class="about-body">
    <h3>Property Management Elk Grove, Sacramento &amp; Surrounding Areas</h3>
    <p>Whether you are an experienced investor or a first-time home owner, we can help you find the right tenants for your property. Our local team handles leasing, repairs and rent collection so you can relax.</p>
    <ul class="checks">
      <li><svg width="12" height="12" viewBox="0 0 12 12"><circle cx="6" cy="6" r="6" fill="#b3121b"/><path d="M3.2 6.2l1.9 1.8 3.7-4" stroke="#fff" stroke-width="1.4" fill="none"/></svg>Sacramento</li>
      <li><svg width="12" height="12" viewBox="0 0 12 12"><circle cx="6" cy="6" r="6" fill="#b3121b"/><path d="M3.2 6.2l1.9 1.8 3.7-4" stroke="#fff" stroke-width="1.4" fill="none"/></svg>El Dorado Hills</li>
      <li><svg width="12" height="12" viewBox="0 0 12 12"><circle cx="6" cy="6" r="6" fill="#b3121b"/><path d="M3.2 6.2l1.9 1.8 3.7-4" stroke="#fff" stroke-width="1.4" fill="none"/></svg>Elk Grove</li>
      <li><svg width="12" height="12" viewBox="0 0 12 12"><circle cx="6" cy="6" r="6" fill="#b3121b"/><path d="M3.2 6.2l1.9 1.8 3.7-4" stroke="#fff" stroke-width="1.4" fill="none"/></svg>Folsom</li>
      <li><svg width="12" height="12" viewBox="0 0 12 12"><circle cx="6" cy="6" r="6" fill="#b3121b"/><path d="M3.2 6.2l1.9 1.8 3.7-4" stroke="#fff" stroke-width="1.4" fill="none"/></svg>Carmichael</li>
      <li><svg width="12" height="12" viewBox="0 0 12 12"><circle cx="6" cy="6" r="6" fill="#b3121b"/><path d="M3.2 6.2l1.9 1.8 3.7-4" stroke="#fff" stroke-width="1.4" fill="none"/></svg>Oak Park</li>
      <li><svg width="12" height="12" viewBox="0 0 12 12"><circle cx="6" cy="6" r="6" fill="#b3121b"/><path d="M3.2 6.2l1.9 1.8 3.7-4" stroke="#fff" stroke-width="1.4" fill="none"/></svg>Citrus Heights</li>
      <li><svg width="12" height="12" viewBox="0 0 12 12"><circle cx="6" cy="6" r="6" fill="#b3121b"/><path d="M3.2 6.2l1.9 1.8 3.7-4" stroke="#fff" stroke-width="1.4" fill="none"/></svg>Auburn</li>
      <li><svg width="12" height="12" viewBox="0 0 12 12"><circle cx="6" cy="6" r="6" fill="#b3121b"/><path d="M3.2 6.2l1.9 1.8 3.7-4" stroke="#fff" stroke-width="1.4" fill="none"/></svg>El Dorado County</li>
      <li><svg width="12" height="12" viewBox="0 0 12 12"><circle cx="6" cy="6" r="6" fill="#b3121b"/><path d="M3.2 6.2l1.9 1.8 3.7-4" stroke="#fff" stroke-width="1.4" fill="none"/></svg>Fairfield County</li>
    </ul>
    <span class="btn">Read More</span>
  </div>
</section>

<section class="listing">
  <h2 class="section-title">Listing</h2>
  <p class="listing-lead">Browse our latest homes for rent, from cozy apartments to family houses. Each listing is checked, cleaned and ready for move-in with clear terms.</p>
  <svg class="slider-arrow" style="left:80px" viewBox="0 0 24 24"><circle cx="12" cy="12" r="12" fill="#e6e6e6"/><path d="M14 7l-5 5 5 5" stroke="#555" stroke-width="2" fill="none"/></svg>
  <svg class="slider-arrow" style="left:1096px" viewBox="0 0 24 24"><circle cx="12" cy="12" r="12" fill="#1c1c1c"/><path d="M10 7l5 5-5 5" stroke="#fff" stroke-width="2" fill="none"/></svg>
  <div class="cards">
    <article class="card">
      <div class="card-photo" role="img" aria-label="Row of suburban townhouses under blue sky" style="background:linear-gradient(180deg,#86b1d6,#c8a484 60%,#7b8f62)"></div>
      <h4>Apartment with Suburbs</h4>
      <p>Bright two-bedroom home close to schools and parks, with a private yard and parking space.</p>
      <div class="card-meta"><span>▣ 3 Beds</span><span>▢ 2 Baths</span><span>◻ 1,240 sqft</span></div>
    </article>
    <article class="card">
      <div class="card-photo" role="img" aria-label="Open living room with dark sofa and kitchen" style="background:linear-gradient(180deg,#d8d4cd,#7a7670 60%,#3e3b38)"></div>
      <h4>Apartment with Suburbs</h4>
      <p>Modern open-plan living space with new kitchen, laundry room and quiet residential street.</p>
      <div class="card-meta"><span>▣ 2 Beds</span><span>▢ 2 Baths</span><span>◻ 1,080 sqft</span></div>
    </article>
    <article class="card">
      <div class="card-photo" role="img" aria-label="Empty bright room with wooden floor" style="background:linear-gradient(180deg,#efe6d8,#c9b79a 60%,#8f6f4c)"></div>
      <h4>Apartment with Suburbs</h4>
      <p>Spacious family unit with wood floors, large windows and easy access to local shops.</p>
      <div class="card-meta"><span>▣ 4 Beds</span><span>▢ 3 Baths</span><span>◻ 1,620 sqft</span></div>
    </article>
  </div>
  <div class="listing-more"><span class="btn">View More Details</span></div>
</section>

<section class="testimonials" role="img" aria-label="Dark city skyline background">
  <h2 class="section-title">Testimonials</h2>
  <svg class="testi-arrow" style="left:110px" viewBox="0 0 22 22"><circle cx="11" cy="11" r="11" fill="#555b62"/><path d="M13 6l-5 5 5 5" stroke="#fff" stroke-width="2" fill="none"/></svg>
  <svg class="testi-arrow" style="left:1068px" viewBox="0 0 22 22"><circle cx="11" cy="11" r="11" fill="#555b62"/><path d="M9 6l5 5-5 5" stroke="#fff" stroke-width="2" fill="none"/></svg>
  <div class="quotes">
    <div class="quote"><div class="quote-mark">“</div><p>The team made renting our home easy. They answered every question fast and found great tenants for us within weeks.</p><div class="author"><span class="avatar" role="img" aria-label="Client portrait"></span>Daniel Harper</div></div>
    <div class="quote"><div class="quote-mark">“</div><p>Friendly, honest and always on time. Repairs were handled quickly and our family felt at home from day one.</p><div class="author"><span class="avatar" role="img" aria-label="Client portrait"></span>Daniel Harper</div></div>
    <div class="quote"><div class="quote-mark">“</div><p>Clear monthly reports and a caring staff. I would recommend their property service to any owner nearby.</p><div class="author"><span class="avatar" role="img" aria-label="Client portrait"></span>Daniel Harper</div></div>
  </div>
</section>

<section class="contact">
  <div class="contact-info">
    <div class="contact-kicker">Information</div>
    <h2>Contact Us</h2>
    <h5>Maple Keys Property Management Inc.</h5>
    <div class="info-row"><svg width="12" height="14" viewBox="0 0 12 14"><path d="M6 0a5 5 0 0 0-5 5c0 4 5 9 5 9s5-5 5-9a5 5 0 0 0-5-5z" fill="#b3121b"/><circle cx="6" cy="5" r="1.8" fill="#fff"/></svg><span>48 Alder Lane, 3rd Floor, Willow Court, NY</span></div>
    <div class="info-row"><svg width="12" height="12" viewBox="0 0 12 12"><rect x="0" y="2" width="12" height="8" rx="1" fill="#b3121b"/><path d="M0.5 2.5l5.5 4 5.5-4" stroke="#fff" fill="none"/></svg><span>hello@maplekeys.biz</span></div>
    <div class="call-label">Call Directly :</div>
    <div class="call-number">+ 44 (0) 300 555 0192</div>
  </div>
  <div class="contact-form">
    <div class="field">First Name</div>
    <div class="field">Last Name</div>
    <div class="field">Email</div>
    <div class="field">Phone</div>
    <div class="field message">Message</div>
    <div class="submit"><span class="btn">Submit</span></div>
  </div>
</section>

<footer class="site-footer">
  <span>© 2024 Maple Keys. All Right Reserved.</span>
  <div class="socials"><span></span><span></span><span></span></div>
</footer>

</div>
</body>
</html>
```